Commercial Solar Flyer

We are an electrical and solar company that requires a flyer that focuses on energy efficient options available including solar that will be primarily for schools and other business owners.
I have a brief attached that gives basics including logo, pictures etc
Also attached is a recent flyer that lists additional services
This is a really urgent request.

Target Market(s)

Business decision makers - 45+ years prominently male
i.e. school principals and / or accountants

Industry/Entity Type

Electrical

Requirements
Must have
• Clutter free, not too much words
Nice to have
• Prefer 1 page A4

```html
<!DOCTYPE html>
<html lang="en">
<head>
<meta charset="utf-8">
<title>B&amp;R Harwood Electrical and Solar – Control Your Costs</title>
<link href="https://fonts.googleapis.com/css2?family=Oswald:wght@400;500&family=Open+Sans:wght@400;700&display=swap" rel="stylesheet">
<style>
  :root {
    --red: #b3282d;
    --red-dark: #8e1f22;
    --ink: #231f20;
    --grey-text: #8a8a8a;
    --grey-light: #e6e6e6;
    --white: #ffffff;
  }
  * { margin: 0; padding: 0; box-sizing: border-box; }
  html, body { width: 849px; height: 1200px; overflow: hidden; background: var(--white); }
  .flyer { position: relative; width: 849px; height: 1200px; overflow: hidden; font-family: "Open Sans", Arial, sans-serif; }

  /* Header */
  .brand { position: absolute; left: 30px; top: 58px; display: flex; align-items: center; gap: 12px; }
  .brand-mark { width: 30px; height: 30px; background: var(--red); }
  .brand-name { font-family: "Oswald", "Arial Narrow", sans-serif; font-weight: 500; font-size: 27px; line-height: 1.05; color: var(--ink); letter-spacing: .5px; text-transform: uppercase; }

  .contact { position: absolute; left: 598px; top: 44px; list-style: none; }
  .contact li { display: flex; align-items: center; gap: 18px; font-size: 15px; color: #333; height: 24px; }
  .contact li.phone { font-weight: 700; font-size: 21px; color: var(--red); height: 30px; letter-spacing: .5px; }
  .contact svg { width: 14px; height: 14px; flex: none; }

  .header-strip { position: absolute; left: 0; top: 0; }

  /* Banner */
  .banner { position: absolute; left: 0; top: 150px; width: 849px; height: 165px; }
  .banner-photo { position: absolute; inset: 0; background: linear-gradient(100deg, #c53a35 0%, #b02c2a 45%, #c9453c 75%, #a52623 100%); }
  .banner-title { position: absolute; left: 0; width: 100%; text-align: center; font-family: "Oswald", "Arial Narrow", sans-serif; font-weight: 400; color: var(--white); font-size: 40px; letter-spacing: .5px; line-height: 1; text-transform: uppercase; }
  .banner-title.top { top: 33px; }
  .banner-title.bottom { top: 98px; }
  .banner-rule { position: absolute; left: 262px; top: 83px; }

  /* Services column */
  .services { position: absolute; left: 30px; top: 362px; width: 220px; }
  .services h2 { font-family: "Oswald", "Arial Narrow", sans-serif; font-weight: 400; font-size: 27px; color: var(--red); line-height: 1; margin-bottom: 21px; }
  .services ul { list-style: none; }
  .services li { position: relative; padding-left: 22px; font-family: "Oswald", "Arial Narrow", sans-serif; font-weight: 400; font-size: 22px; line-height: 27px; color: var(--grey-text); text-transform: uppercase; margin-bottom: 12.5px; }
  .services li::before { content: ""; position: absolute; left: 2px; top: 12px; width: 5px; height: 5px; border-radius: 50%; background: var(--grey-text); }

  .social { position: absolute; left: 28px; top: 1141px; width: 204px; border-top: 1px solid #bbb; padding-top: 10px; display: flex; align-items: center; gap: 8px; font-size: 15px; color: var(--red); }
  .social-label { margin-right: 4px; }
  .social-square { width: 22px; height: 22px; background: var(--red); margin-right: 4px; }

  /* Dark panel */
  .panel { position: absolute; left: 272px; top: 315px; width: 577px; height: 885px; background: var(--ink); }
  .panel-photo { position: absolute; left: 272px; top: 600px; width: 577px; height: 600px; background: linear-gradient(180deg, rgba(35,31,32,0) 0%, rgba(70,70,72,.35) 45%, #5a5b5e 62%, #9a9b9e 82%, #c4c5c8 100%); }
  .red-bar { position: absolute; left: 0; top: 0; }

  .intro { position: absolute; left: 297px; top: 368px; width: 505px; color: var(--white); font-size: 15.5px; line-height: 22px; }
  .intro p + p { margin-top: 10px; }

  .benefits-title { position: absolute; left: 297px; top: 648px; font-family: "Oswald", "Arial Narrow", sans-serif; font-weight: 400; font-size: 25px; color: var(--white); line-height: 32px; text-transform: uppercase; }

  .benefits { position: absolute; left: 297px; top: 707px; width: 500px; list-style: none; color: var(--white); font-size: 15.5px; line-height: 19px; }
  .benefits li { position: relative; padding-left: 23px; margin-bottom: 11px; }
  .benefits li::before { content: ""; position: absolute; left: 2px; top: 6px; width: 0; height: 0; border-left: 6px solid var(--red); border-top: 4px solid transparent; border-bottom: 4px solid transparent; }
</style>
</head>
<body>
<main class="flyer">

  <svg class="header-strip" width="849" height="152" viewBox="0 0 849 152" aria-hidden="true">
    <polygon points="470,152 520,138 849,138 849,152" fill="var(--grey-light)"/>
  </svg>

  <header>
    <div class="brand">
      <span class="brand-mark" aria-hidden="true"></span>
      <span class="brand-name">B&amp;R Harwood<br>Electrical and Solar</span>
    </div>
    <ul class="contact">
      <li class="phone">
        <svg viewBox="0 0 16 16" aria-hidden="true"><path d="M3 1c1 0 3 3 3 4s-2 1-1 3 2 3 3 3 1-2 2-1 3 2 3 3-2 2-3 2C7 15 1 9 1 4c0-1 1-3 2-3z" fill="var(--red)"/></svg>
        1300 555 014
      </li>
      <li>
        <svg viewBox="0 0 16 16" aria-hidden="true"><rect x="1" y="3" width="14" height="10" fill="#777"/><path d="M1 3l7 6 7-6" stroke="#fff" stroke-width="1.3" fill="none"/></svg>
        jess@harwoodsolar.com.au
      </li>
      <li>
        <svg viewBox="0 0 16 16" aria-hidden="true"><g fill="none" stroke="#777" stroke-width="1.3"><circle cx="8" cy="8" r="6.5"/><ellipse cx="8" cy="8" rx="3" ry="6.5"/><path d="M1.5 8h13M2.5 4.5h11M2.5 11.5h11"/></g></svg>
        www.brelectrical.com.au
      </li>
    </ul>
  </header>

  <section class="banner">
    <div class="banner-photo" role="img" aria-label="Red-tinted photo of company service vans parked outside the depot"></div>
    <h1 class="banner-title top">Control Your Costs</h1>
    <svg class="banner-rule" width="326" height="10" viewBox="0 0 326 10" aria-hidden="true">
      <line x1="0" y1="5" x2="326" y2="5" stroke="#fff" stroke-width="1"/>
      <rect x="155" y="1" width="3" height="8" fill="#fff"/>
      <rect x="168" y="1" width="3" height="8" fill="#fff"/>
    </svg>
    <p class="banner-title bottom">Free Consultation</p>
  </section>

  <aside class="services">
    <h2>OUR SERVICES</h2>
    <ul>
      <li>Solar Power</li>
      <li>Power Factor Correction</li>
      <li>Peak Power Management</li>
      <li>Energy Efficient Solutions</li>
      <li>Design and Install</li>
      <li>Thermal Imaging</li>
      <li>Exit &amp; Emergency Audits</li>
      <li>Energy Efficient Audits</li>
      <li>RCD Audits</li>
      <li>Onload Testing</li>
      <li>LED Lighting</li>
      <li>Renovations and Refits</li>
      <li>Data and TV</li>
      <li>24HR Service</li>
    </ul>
  </aside>

  <div class="social">
    <span class="social-label">Like us:</span>
    <span class="social-square" aria-hidden="true"></span>
    <span class="social-square" aria-hidden="true"></span>
    <span class="social-square" aria-hidden="true"></span>
  </div>

  <div class="panel"></div>
  <div class="panel-photo" role="img" aria-label="Transmission tower and rooftop solar panel array with a heritage building in the distance"></div>

  <svg class="red-bar" width="849" height="1200" viewBox="0 0 849 1200" aria-hidden="true">
    <polygon points="257,545 272,560 272,1200 257,1200" fill="var(--red)"/>
    <polygon points="257,645 585,645 548,683 257,683" fill="var(--red)"/>
  </svg>

  <section class="intro">
    <p>B&amp;R Harwood Electrical and Solar is a Queensland based company providing energy efficient electrical and solar services for Commercial and residential customers. Our goal is to provide a customised and complete energy efficient solution to our customers rather than just a solar package like most other solar marketing companies.</p>
    <p>Electricity prices are still rising and many businesses are looking to solar as a way of controlling their ongoing costs. But there are many other ways to reduce and control costs including Power Factor Correction, Static Compensation ,Peak Power Management, LED Lighting and Solar Hot Water.</p>
  </section>

  <h2 class="benefits-title">Key Benefits</h2>
  <ul class="benefits">
    <li>All products of high quality and Green Grid Standards Board (GGSB) members</li>
    <li>From initial contact we design, install, maintain and repair for the life of the system</li>
    <li>Competitively priced</li>
    <li>Fully Insured</li>
    <li>Accredited Master Electricians</li>
    <li>Triple Certification – Health, Safety and Environmental accredited</li>
  </ul>

</main>
</body>
</html>
```